Website - Corla Druvick

I need a website that has multiple pages and easy for me to update pictures, content and blogs as an ongoing basis’s.
It will have videos and needs to be compatible to view easily and aesthetically on mobile phones.
Please refer to this website for inspiration www.lorettaquisp.com

Coding

Coded - Design and coding required

Number of Pages Required

5+ page

Font styles to use
Other font styles liked:
• Refer to website provided as inspiration

Requirements
Must have
• Please use stock images for now to do design, but I will be providing all imagery, videos and content

```html
<!DOCTYPE html>
<html lang="en">
<head>
<meta charset="utf-8">
<title>Corla Druvick</title>
<link href="https://fonts.googleapis.com/css2?family=Delius&family=Raleway:wght@400;600;700;800&family=Lato:wght@400;700&display=swap" rel="stylesheet">
<style>
:root{
  --accent:#f2434e;
  --ink:#1f1f1f;
  --muted:#7a7a7a;
  --card:#f8f8fb;
  --footer:#f6f6fa;
  --line:#e4e4e8;
  --white:#ffffff;
}
*{box-sizing:border-box;margin:0;padding:0}
html,body{width:1200px;height:2582px;overflow:hidden}
body{position:relative;font-family:'Lato',sans-serif;color:var(--ink);background:var(--white)}
.abs{position:absolute}

/* hero */
.hero{left:0;top:0;width:1200px;height:668px;background:linear-gradient(180deg,#8fb1bd 0%,#a7b6ae 30%,#9a7a4a 52%,#7d5a30 80%,#5b3f22 100%)}
.brand{left:116px;top:28px;font-family:'Delius',cursive;font-size:32px;color:var(--white)}
.nav{right:0;top:32px;display:flex;align-items:center;font-family:'Raleway',sans-serif;font-size:17px;color:#f2f2f2}
.nav a{color:inherit;text-decoration:none;margin-right:37px}
.nav .active{border:1.5px solid #f2f2f2;border-radius:20px;padding:6px 24px;margin-right:27px}
.nav .social{width:20px;height:20px;border:2px solid #f2f2f2;border-radius:50%;margin-right:118px}
.arrow-btn{width:38px;height:38px;border:1.5px solid #fff;border-radius:50%;top:318px;display:flex;align-items:center;justify-content:center}
.hero-title{left:0;width:1200px;top:318px;text-align:center;font-family:'Raleway',sans-serif;font-weight:800;font-size:48px;color:#fff;letter-spacing:-1px}
.hero-sub{left:0;width:1200px;top:380px;text-align:center;font-family:'Raleway',sans-serif;font-size:48px;color:#fff;letter-spacing:-1px}
.hero-tag{left:0;width:1200px;top:455px;text-align:center;font-family:'Raleway',sans-serif;font-size:15px;color:#fff}
.hero-btn{left:524px;top:509px;width:151px;height:32px;border-radius:16px;background:var(--accent);color:#fff;font-family:'Raleway',sans-serif;font-weight:700;font-size:11px;letter-spacing:1px;display:flex;align-items:center;justify-content:center}
.mouse{left:593px;top:622px;width:10px;height:18px;border:1.5px solid #fff;border-radius:5px}

/* posts */
.section-title{left:173px;top:725px;font-family:'Raleway',sans-serif;font-size:44px;font-weight:400}
.section-title b{font-weight:800}
.search{left:784px;top:737px;width:243px;height:36px;background:#e2e2e2;border-radius:3px;font-size:14px;color:#333;padding:0 18px;display:flex;align-items:center;justify-content:space-between}
.rule{left:172px;top:798px;width:856px;height:1px;background:var(--line)}
.posts{left:172px;top:841px;display:grid;grid-template-columns:repeat(3,269px);column-gap:23px;row-gap:23px}
.post{width:269px;height:295px;background:var(--card)}
.post.hover{background:#fff;box-shadow:0 4px 12px rgba(0,0,0,.12)}
.thumb{height:198px;position:relative}
.play{position:absolute;left:115px;top:79px;width:40px;height:40px;border-radius:50%;background:rgba(40,40,40,.75)}
.play svg{position:absolute;left:13px;top:11px}
.post h3{font-family:'Raleway',sans-serif;font-weight:700;font-size:16px;margin:22px 19px 0}
.post.hover h3{color:var(--accent)}
.meta{display:flex;justify-content:space-between;margin:20px 22px 0 19px;font-size:12.5px;color:var(--muted)}
.t1{background:linear-gradient(135deg,#6f6f6a,#b9875a 60%,#3e4a34)}
.t2{background:linear-gradient(180deg,#b9b9b2,#8e8a7f 50%,#c8a781)}
.t3{background:linear-gradient(135deg,#c9b4b9,#6b4a3f 55%,#d16a6a)}
.t4{background:linear-gradient(135deg,#cfcdcb,#8c7a6c 55%,#3a3532)}
.t5{background:linear-gradient(135deg,#e6d6d1,#a68073 50%,#4a3a36)}
.t6{background:linear-gradient(180deg,#dcdedf,#a9aeb3 60%,#595d69)}
.t7{background:linear-gradient(135deg,#bfc4c8,#b98f78 55%,#4f4a48)}
.t8{background:linear-gradient(135deg,#d9dcde,#b8bfc4 50%,#7fc7c5)}
.t9{background:linear-gradient(180deg,#e5e6e6,#9a9590 55%,#3a3633)}

/* pagination */
.pager{left:0;width:1200px;top:1824px;display:flex;justify-content:center;align-items:center;font-size:10px;font-family:'Raleway',sans-serif;font-weight:600}
.pager .prev{margin-right:74px}
.pager .pg{width:23px;height:23px;border:1px solid #ccc;display:flex;align-items:center;justify-content:center;margin-right:5px}
.pager .pg.on{background:var(--accent);border-color:var(--accent);color:#fff}
.pager .next{margin-left:72px;text-decoration:underline}

/* feed */
.feed-line{left:172px;top:1926px;width:856px;height:1px;background:var(--line)}
.feed-title{left:470px;top:1914px;width:260px;background:#fff;text-align:center;font-family:'Raleway',sans-serif;font-weight:700;font-size:14px}
.feed{left:172px;top:1960px;display:flex;gap:3px}
.feed div{width:140px;height:140px}
.f1{background:linear-gradient(135deg,#c9d5e0,#a07c6a)}
.f2{background:linear-gradient(135deg,#8b7a6c,#d8cfc5)}
.f3{background:linear-gradient(135deg,#efc8c5,#b08561)}
.f4{background:linear-gradient(135deg,#6d6660,#c8bab0)}
.f5{background:linear-gradient(135deg,#c9d5e0,#a07c6a)}
.f6{background:linear-gradient(180deg,#e6eaee,#7a4a36)}

/* footer */
.footer{left:0;top:2153px;width:1200px;height:357px;background:var(--footer)}
.top-btn{left:1022px;top:2170px;width:36px;height:36px;border-radius:50%;background:var(--accent)}
.top-label{left:1000px;top:2213px;width:80px;text-align:center;font-size:9px;font-weight:700}
.fh{top:2258px;font-family:'Raleway',sans-serif;font-weight:700;font-size:16px}
.ftxt{font-size:11px;line-height:18px;color:#444;letter-spacing:-.2px}
.links{left:334px;top:2293px;font-size:10.5px;font-weight:700;line-height:24px;color:#333;list-style:none}
.email{left:478px;top:2302px;width:209px;height:45px;border:1.5px solid #ccc;background:#fff;font-size:14px;color:#777;display:flex;align-items:center;padding-left:23px}
.sub-btn{left:478px;top:2356px;width:209px;height:44px;background:var(--accent);color:#fff;font-size:14px;display:flex;align-items:center;justify-content:space-between;padding:0 20px}
.rp{display:flex;gap:14px;width:145px}
.rp i{display:block;width:47px;height:47px;flex:none}
.rp span{font-size:12px;line-height:16px;color:#333}
.copy{left:0;width:1200px;top:2532px;text-align:center;font-size:12px;color:#555}
</style>
</head>
<body>

<div class="abs hero" role="img" aria-label="Woman in a straw hat smiling in a golden wheat field"></div>
<div class="abs brand">Corla Druvick</div>
<nav class="abs nav">
  <a class="active">About</a><a>Show Reels</a><a>Tea With T</a><a>Contact</a><span class="social"></span>
</nav>
<div class="abs arrow-btn" style="left:121px"><svg width="10" height="10" viewBox="0 0 10 10"><path d="M6 2 3 5l3 3" stroke="#fff" stroke-width="1.5" fill="none"/></svg></div>
<div class="abs arrow-btn" style="left:1038px"><svg width="10" height="10" viewBox="0 0 10 10"><path d="M4 2l3 3-3 3" stroke="#fff" stroke-width="1.5" fill="none"/></svg></div>
<h1 class="abs hero-title">Events &amp; Meetings</h1>
<p class="abs hero-sub">to improve your business model</p>
<p class="abs hero-tag">PARTICIPANTS AND SPEAKERS WELCOME</p>
<div class="abs hero-btn">OUR VIDEOS</div>
<div class="abs mouse"></div>

<h2 class="abs section-title">Latest <b>Posts...</b></h2>
<div class="abs search">Search <svg width="10" height="6" viewBox="0 0 10 6"><path d="M1 1l4 4 4-4" stroke="#444" fill="none"/></svg></div>
<div class="abs rule"></div>

<div class="abs posts">
  <article class="post"><div class="thumb t1" role="img" aria-label="Woman in a plaid jacket on a city street"><span class="play"><svg width="16" height="18"><path d="M2 1l13 8-13 8z" fill="#f2434e"/></svg></span></div><h3>Tea With T</h3><div class="meta"><span>Admin</span><span>2 Comments</span></div></article>
  <article class="post hover"><div class="thumb t2" role="img" aria-label="Friends running into the sea on a beach"><span class="play"><svg width="16" height="18"><path d="M2 1l13 8-13 8z" fill="#f2434e"/></svg></span></div><h3>Dance</h3><div class="meta"><span>Admin</span><span>2 Comments</span></div></article>
  <article class="post"><div class="thumb t3" role="img" aria-label="Two friends laughing by a painted wall"><span class="play"><svg width="16" height="18"><path d="M2 1l13 8-13 8z" fill="#f2434e"/></svg></span></div><h3>Act</h3><div class="meta"><span>Admin</span><span>2 Comments</span></div></article>
  <article class="post"><div class="thumb t4" role="img" aria-label="Model with curly hair in a leather jacket"><span class="play"><svg width="16" height="18"><path d="M2 1l13 8-13 8z" fill="#f2434e"/></svg></span></div><h3>Model</h3><div class="meta"><span>Admin</span><span>2 Comments</span></div></article>
  <article class="post"><div class="thumb t5" role="img" aria-label="Woman leaning on a wall with confetti"><span class="play"><svg width="16" height="18"><path d="M2 1l13 8-13 8z" fill="#f2434e"/></svg></span></div><h3>Tea With T</h3><div class="meta"><span>Admin</span><span>2 Comments</span></div></article>
  <article class="post"><div class="thumb t6" role="img" aria-label="Woman walking along a misty shoreline"><span class="play"><svg width="16" height="18"><path d="M2 1l13 8-13 8z" fill="#f2434e"/></svg></span></div><h3>Tea With T</h3><div class="meta"><span>Admin</span><span>2 Comments</span></div></article>
  <article class="post"><div class="thumb t7" role="img" aria-label="Woman taking a selfie on a sunny street"><span class="play"><svg width="16" height="18"><path d="M2 1l13 8-13 8z" fill="#f2434e"/></svg></span></div><h3>Model</h3><div class="meta"><span>Admin</span><span>2 Comments</span></div></article>
  <article class="post"><div class="thumb t8" role="img" aria-label="Birthday celebration with silver number balloons"><span class="play"><svg width="16" height="18"><path d="M2 1l13 8-13 8z" fill="#f2434e"/></svg></span></div><h3>Dance</h3><div class="meta"><span>Admin</span><span>2 Comments</span></div></article>
  <article class="post"><div class="thumb t9" role="img" aria-label="Person walking on a dark sand beach"><span class="play"><svg width="16" height="18"><path d="M2 1l13 8-13 8z" fill="#f2434e"/></svg></span></div><h3>Act</h3><div class="meta"><span>Admin</span><span>2 Comments</span></div></article>
</div>

<div class="abs pager">
  <span class="prev">&laquo;&nbsp;&nbsp; Previous</span>
  <span class="pg">1</span><span class="pg">2</span><span class="pg on">3</span><span class="pg">4</span>
  <span class="next">Next</span><span>&nbsp;&nbsp;&raquo;</span>
</div>

<div class="abs feed-line"></div>
<div class="abs feed-title">Follow @ Lensfeed</div>
<div class="abs feed">
  <div class="f1" role="img" aria-label="Hand holding a glass ball over a city"></div>
  <div class="f2" role="img" aria-label="Woman in sunglasses by a graffiti wall"></div>
  <div class="f3" role="img" aria-label="Bearded man holding a flower"></div>
  <div class="f4" role="img" aria-label="Woman in sunglasses posing outdoors"></div>
  <div class="f5" role="img" aria-label="Hand holding a glass ball over a city"></div>
  <div class="f6" role="img" aria-label="Person in a cap and hoodie by the sea"></div>
</div>

<footer class="abs footer"></footer>
<div class="abs top-btn"><svg width="36" height="36"><path d="M14 20l4-4 4 4" stroke="#fff" stroke-width="1.6" fill="none"/></svg></div>
<div class="abs top-label">Back to Top</div>

<h4 class="abs fh" style="left:161px">Our Address</h4>
<p class="abs ftxt" style="left:161px;top:2295px;width:130px">48/ 9 Marlow Lane Studio. 22/C Harbour Row, Eastfield.</p>
<p class="abs ftxt" style="left:161px;top:2365px">+44-020 7946 015<br>hello@corladruvick.com</p>

<h4 class="abs fh" style="left:334px">Quick Links</h4>
<ul class="abs links"><li>Home</li><li>About Us</li><li>Show Reels</li><li>Tea With T</li><li>Contact Us</li></ul>

<h4 class="abs fh" style="left:476px">Subscribe Now</h4>
<div class="abs email">Enter email Address</div>
<div class="abs sub-btn">SUBSCRIBE NOW <svg width="22" height="12"><path d="M0 6h20M15 1l5 5-5 5" stroke="#fff" fill="none"/></svg></div>

<h4 class="abs fh" style="left:751px">Recent Posts</h4>
<div class="abs rp" style="left:751px;top:2296px"><i style="background:linear-gradient(135deg,#dfe3df,#6d7a5e)" role="img" aria-label="Person in a green field"></i><span>Visiting Green Field</span></div>
<div class="abs rp" style="left:901px;top:2296px"><i style="background:linear-gradient(135deg,#9aa496,#3d4a3a)" role="img" aria-label="Flower arrangement outdoors"></i><span>Simple Flower Arements You Can Put .</span></div>
<div class="abs rp" style="left:751px;top:2369px"><i style="background:linear-gradient(180deg,#eceff2,#6a5a3e)" role="img" aria-label="Traveller on a rocky hill"></i><span>Europe's best affordab</span></div>
<div class="abs rp" style="left:902px;top:2367px"><i style="background:linear-gradient(135deg,#dfe3df,#6d7a5e)" role="img" aria-label="Person in a green field"></i><span>Visiting Green Field</span></div>

<p class="abs copy">Copyright © 2021 Corla Druvick. All Rights Reserved.</p>

</body>
</html>
```